Motivational Poster Design Project

I would like to create a poster with some of my favorite quotes to hang in my office.

Industry/Entity Type

Quotes

Requirements
Must have
• The poster will be 24" high x 36" long and printed on canvas, so the image you create needs to have a resolution of at least 2700 x 3900.

The poster must contain the following quotes:

“Your beliefs become your thoughts,
Your thoughts become your words,
Your words become your actions,
Your actions become your habits,
Your habits become your values,
Your values become your destiny.”
-Varuna Pellath

"Winners practice until they get it right. Champions practice until they can’t get it wrong!"
-Unknown

"Style is the perfection of a point of view."
-Conrad Whitlowe

"My interest in life comes from setting myself huge, apparently unachieveable challenges and trying to rise above them."
-Sir Oswin Talbrook

"Problems cannot be solved by the same level of thinking that created them."
-Gustav Morrendel

"People think focus means saying yes to the thing you've got to focus on. But that's not what it means at all. It means saying no to the hundred other good ideas that there are. You have to pick carefully."
-Dale Parrick

"Think like a man of action and act like a man of thought."
-Lucien Marvaud
Nice to have
• It would be nice to have an image of each person who is being quoted (if known) along with the quote that is attributable to them.

```html
<!DOCTYPE html>
<html lang="en">
<head>
<meta charset="utf-8">
<title>Quotes Poster</title>
<link rel="stylesheet" href="https://fonts.googleapis.com/css2?family=Cinzel:wght@400;700&family=Great+Vibes&family=Josefin+Slab:wght@400;600&family=Oswald:wght@300&family=Tinos&display=swap">
<style>
  :root {
    --ink: #000000;
    --paper: #ffffff;
    --quote-yellow: #f4e200;
    --mark-yellow: #f6e80a;
    --script-blue: #1336f0;
    --magenta: #e0189c;
    --circle-magenta: rgba(176, 40, 160, 0.88);
    --photo-light: #bdbdbd;
    --photo-mid: #7a7a7a;
  }
  * { margin: 0; padding: 0; box-sizing: border-box; }
  html, body { width: 800px; height: 1200px; overflow: hidden; background: var(--ink); }
  .poster { position: relative; width: 800px; height: 1200px; overflow: hidden; background: var(--ink); }
  .photo { position: absolute; }

  .photo--belief { left: 0; top: 0; width: 800px; height: 470px;
    clip-path: polygon(0 0, 800px 0, 800px 455px, 0 172px);
    background: linear-gradient(100deg, var(--photo-mid) 0%, var(--photo-light) 40%, #9a9a9a 70%, #6d6d6d 100%); }
  .divider-diagonal { left: 0; top: 0; width: 800px; height: 480px; background: var(--paper);
    clip-path: polygon(0 170px, 800px 448px, 800px 468px, 0 192px); }
  .photo--style { left: 0; top: 0; width: 800px; height: 590px;
    clip-path: polygon(0 192px, 800px 468px, 800px 584px, 0 582px);
    background: radial-gradient(ellipse at 28% 55%, #8c8c8c 0%, #3c3c3c 45%, #141414 85%); }
  .divider-flat { left: 0; top: 586px; width: 800px; height: 12px; background: var(--paper);
    clip-path: polygon(0 0, 800px 3px, 800px 12px, 0 9px); }

  .photo--problems { left: 0; top: 600px; width: 326px; height: 335px;
    background: radial-gradient(ellipse at 45% 40%, #c8c8c8 0%, #6e6e6e 45%, #1e1e1e 90%); }
  .photo--thought { left: 326px; top: 600px; width: 264px; height: 330px;
    background: radial-gradient(ellipse at 40% 35%, #9a9a9a 0%, #4a4a4a 40%, #0e0e0e 85%); }
  .pattern--winners { left: 590px; top: 600px; width: 210px; height: 110px;
    background: linear-gradient(160deg, #c9c9c9 0%, #7a6a6a 30%, #4a3a48 60%, #000 100%); }
  .photo--focus { left: 395px; top: 935px; width: 405px; height: 220px;
    background: radial-gradient(ellipse at 55% 40%, #8a8a8a 0%, #3a3a3a 40%, #0a0a0a 80%); }
  .bottom-cap { left: 0; top: 1090px; width: 800px; height: 110px; background: var(--ink);
    clip-path: polygon(40px 110px, 348px 24px, 800px 38px, 800px 110px); }

  .quote { position: absolute; }
  .quote--belief { left: 313px; top: 48px; font-family: "Tinos", Georgia, serif;
    font-size: 24.5px; line-height: 27.6px; letter-spacing: 0.4px; color: var(--paper); white-space: nowrap; }
  .mark { position: absolute; font-family: "Tinos", Georgia, serif; font-weight: 700;
    color: var(--mark-yellow); font-size: 64px; line-height: 1; }
  .mark--open { left: 250px; top: 12px; }
  .mark--close { left: 734px; top: 196px; }
  .author--script { position: absolute; left: 428px; top: 238px; font-family: "Great Vibes", cursive;
    font-size: 50px; letter-spacing: 2px; color: var(--script-blue); white-space: nowrap; }

  .quote--style { left: 388px; top: 420px; color: var(--paper); font-family: "Josefin Slab", serif; white-space: nowrap; }
  .quote--style .line { display: block; font-size: 54px; line-height: 40px; letter-spacing: -0.5px; }
  .quote--style .line + .line { margin-left: 22px; }
  .quote--style .keyword { font-family: "Oswald", sans-serif; font-weight: 300; font-size: 66px;
    letter-spacing: -2px; vertical-align: -2px; }
  .author--style { position: absolute; left: 597px; top: 563px; font-family: "Tinos", serif;
    font-size: 15px; color: var(--paper); white-space: nowrap; }

  .circle { position: absolute; left: 44px; top: 702px; width: 234px; height: 234px; border-radius: 50%;
    background: var(--circle-magenta); }
  .quote--problems { left: 50px; top: 768px; width: 228px; text-align: center; font-family: "Cinzel", serif;
    font-size: 15px; line-height: 17px; color: var(--paper); text-transform: uppercase; white-space: nowrap; }
  .quote--thought { left: 372px; top: 764px; width: 212px; text-align: center; font-family: "Cinzel", serif;
    font-size: 25px; line-height: 27px; color: var(--magenta); text-transform: uppercase; white-space: nowrap; }
  .quote--winners { left: 592px; top: 694px; width: 208px; font-family: "Cinzel", serif; font-weight: 700;
    font-size: 22px; line-height: 24px; color: var(--quote-yellow); text-align: center; white-space: nowrap; }
  .quote--focus { left: 18px; top: 946px; width: 380px; font-family: "Cinzel", serif;
    font-size: 14px; line-height: 19.5px; color: var(--paper); text-transform: uppercase; white-space: nowrap; }
  .quote--challenge { left: 0; top: 1110px; width: 800px; text-align: center; font-family: "Cinzel", serif;
    font-weight: 700; font-size: 15px; line-height: 14.5px; color: var(--paper); text-transform: uppercase; }
</style>
</head>
<body>
<main class="poster">
  <div class="photo photo--belief" role="img" aria-label="Black and white portrait of Varuna Pellath"></div>
  <div class="photo divider-diagonal"></div>
  <div class="photo photo--style" role="img" aria-label="Black and white photograph of Conrad Whitlowe"></div>
  <div class="photo divider-flat"></div>

  <span class="mark mark--open">&ldquo;</span>
  <p class="quote quote--belief">
    Your beliefs become your thoughts,<br>
    Your thoughts become your words,<br>
    Your words become your actions,<br>
    Your actions become your habits,<br>
    Your habits become your values,<br>
    Your values become your destiny.
  </p>
  <span class="mark mark--close">&rdquo;</span>
  <p class="author--script">Varuna Pellath</p>

  <p class="quote quote--style">
    <span class="line"><span class="keyword">STYLE</span>is the</span>
    <span class="line">perfection of</span>
    <span class="line">point of view</span>
  </p>
  <p class="author--style">Conrad Whitlowe</p>

  <div class="photo photo--problems" role="img" aria-label="Black and white portrait of Gustav Morrendel"></div>
  <div class="photo photo--thought" role="img" aria-label="Black and white portrait of Lucien Marvaud"></div>
  <div class="photo pattern--winners" role="img" aria-label="Decorative geometric cube pattern"></div>

  <div class="circle"></div>
  <p class="quote quote--problems">Problems cannot be<br>solved by the same<br>level of thinking<br>that created them.</p>
  <p class="quote quote--thought">&ldquo; Think like<br>a man of<br>action and<br>act like a<br>man of<br>thought. &rdquo;</p>
  <p class="quote quote--winners">"WINNERS<br>PRACTICE<br>UNTIL THEY<br>GET IT RIGHT<br>CHAMPIONS<br>PRACTICE<br>UNTIL THEY<br>CAN&rsquo;T GET<br>IT WRONG!"</p>

  <div class="photo photo--focus" role="img" aria-label="Close-up black and white portrait of Dale Parrick"></div>
  <p class="quote quote--focus">People think focus means saying<br>yes to the thing you've got to<br>focus on. But that's not what it<br>means at all. It means saying no<br>to the hundred other good ideas<br>that there are. You have to pick<br>carefully."</p>

  <div class="photo bottom-cap"></div>
  <p class="quote quote--challenge">
    &ldquo;My<br>
    interest in life<br>
    comes from setting myself<br>
    huge, apparently unachieveable<br>
    challenges and trying to rise above them<br>
    Sir Oswin Talbrook
  </p>
</main>
</body>
</html>
```